Brisk Mend's Blow Their Mind Website

We own a group of cell phone and tablet repair shops in the bay area that is emerging into the mobile device insurance industry and want to develop a site that is clean, organized, and efficient at communicating who we are, the services we provide and the positive feedback we have been getting from our clients. As we enter into this new field of business, Our goal is to attract larger corporate accounts.

We want our home screen to have a big focus on the protection plan for the devices right away much like the home screen from these links:

http://www.gadgetvault.com/

and also - https://us.keepitsnug.com/smartphone-protection.html

We also need to make our repair services clear, here is a website of a company that does repair and we want to highlight both ends of the business.

ww.fixnovo.com

So the home screen will include the tab categories at the top of the screen
home/ protection /repair /about /contact

The first portion will be protection and as you scroll down there will be the next section about repair and following that will be information about the company.

Target Market(s)

Individuals that would be looking for pricing, clients that come to our store, but ultimately the heavy hitters we would want to attract would be larger corporate accounts so the message we want to communicate is professional, organized and credible in the services we provide.

Industry/Entity Type

Cell Phone

Number of Pages Required

5+ page

Font styles to use
Serif

Colors
34a6d7

Requirements
Must have
• Eye catching, organized, with the wow factor that a business will look at our site and will be able to tell that we know what looks good and what grabs peoples attention. A large emphasis on the protection plan section like the links we provided and an organized home screen with the sections highlighted in the project description
• Tabs with links to different sections of the business such as protection that will go into detail about our protections plans and why our plan is best
• repair with a menu of the different prices we provide for different devices and services for that device
• an about us tab
• a contact us tab
Nice to have
• Artistic flow on the homescreen that the different sections flow together without looking too cookie cutter
• Wow factor
Should not have
• Clutter, confusion, disorganization, cheesy cookie cutter

```html
<!DOCTYPE html>
<html lang="en">
<head>
<meta charset="utf-8">
<title>Brisk Mend – Device Protection &amp; Repair</title>
<link rel="stylesheet" href="https://fonts.googleapis.com/css2?family=Raleway:wght@300;400;600;700&family=Open+Sans:wght@400;600;700&display=swap">
<style>
  :root {
    --brand: #34a6d7;
    --brand-dark: #1f8dbf;
    --ink: #333a40;
    --muted: #7a8288;
    --line: #dfe3e6;
    --panel: #f1f2f3;
    --table-head: #4b5158;
    --white: #ffffff;
    --hero-a: #3d4a3a;
    --hero-b: #8c8a6f;
    --review-a: #7b6a3c;
    --review-b: #c9a95a;
  }
  * { box-sizing: border-box; margin: 0; padding: 0; }
  html, body { width: 1200px; height: 2284px; overflow: hidden; }
  body { position: relative; background: var(--white); color: var(--ink); font-family: "Open Sans", Arial, sans-serif; }
  .abs { position: absolute; }

  /* Header */
  .site-header { position: absolute; left: 0; top: 0; width: 1200px; height: 88px; background: var(--white); }
  .brand { position: absolute; left: 200px; top: 22px; display: flex; align-items: center; gap: 12px; }
  .brand-mark { width: 40px; height: 40px; background: var(--brand); border-radius: 6px; }
  .brand-name { font-family: "Raleway", Arial, sans-serif; font-weight: 600; font-size: 30px; color: var(--brand); }
  .call { position: absolute; right: 200px; top: 24px; text-align: right; }
  .call small { display: block; font-size: 12px; color: var(--muted); }
  .call strong { font-size: 18px; color: var(--brand); font-weight: 600; }

  .main-nav { position: absolute; left: 0; top: 88px; width: 1200px; height: 32px; background: var(--brand); }
  .main-nav ul { list-style: none; display: flex; justify-content: center; height: 100%; }
  .main-nav li { width: 160px; text-align: center; line-height: 32px; color: var(--white); font-size: 13px; font-weight: 600; letter-spacing: 1px; }
  .main-nav li.active { background: var(--brand-dark); }

  /* Hero */
  .hero { position: absolute; left: 0; top: 120px; width: 1200px; height: 472px; background: linear-gradient(100deg, var(--hero-a) 0%, #5b6450 45%, var(--hero-b) 100%); }
  .hero-copy { position: absolute; left: 200px; top: 110px; width: 360px; color: var(--white); }
  .hero-copy h1 { font-family: "Raleway", Arial, sans-serif; font-weight: 300; font-size: 48px; line-height: 1; margin-bottom: 14px; }
  .hero-copy p { font-size: 13px; line-height: 1.5; margin-bottom: 14px; opacity: .9; }
  .hero-copy ul { list-style: none; }
  .hero-copy li { display: flex; align-items: center; gap: 10px; font-size: 13px; margin-bottom: 8px; }
  .tick { width: 18px; height: 18px; border-radius: 50%; background: var(--brand); flex: none; }
  .quote-box { position: absolute; left: 640px; top: 150px; width: 340px; height: 150px; background: rgba(255,255,255,.22); padding: 24px 28px; color: var(--white); }
  .quote-box .label { font-family: "Raleway", Arial, sans-serif; font-size: 24px; font-weight: 300; }
  .quote-box .price { font-family: "Raleway", Arial, sans-serif; font-size: 30px; font-weight: 400; margin-top: 2px; }
  .quote-box .price small { font-size: 22px; }
  .btn { display: inline-block; background: var(--brand); color: var(--white); font-size: 12px; font-weight: 600; padding: 7px 18px; border-radius: 3px; }
  .quote-box .btn { margin-top: 10px; }
  .hero-arrow { position: absolute; top: 300px; }

  /* Pricing */
  .pricing { position: absolute; left: 0; top: 592px; width: 1200px; height: 428px; background: var(--panel); }
  .section-title { font-family: "Raleway", Arial, sans-serif; font-weight: 400; font-size: 26px; text-align: center; color: var(--ink); }
  .pricing .section-title { position: absolute; top: 34px; width: 100%; }
  .compare { position: absolute; left: 200px; top: 88px; width: 800px; border-collapse: collapse; font-size: 11px; background: var(--white); }
  .compare th { height: 64px; color: var(--white); background: var(--table-head); font-weight: 400; border-left: 2px solid var(--panel); }
  .compare th.plan-best { background: var(--brand); }
  .compare th.corner { background: var(--panel); }
  .compare th span { display: block; font-size: 10px; letter-spacing: 1px; opacity: .8; }
  .compare th b { display: block; font-family: "Raleway", Arial, sans-serif; font-size: 30px; font-weight: 600; }
  .compare td { height: 24px; border-top: 1px solid var(--line); text-align: center; color: var(--muted); border-left: 1px solid var(--line); }
  .compare td.row-label { text-align: left; padding-left: 14px; width: 320px; color: var(--ink); border-left: 0; }
  .chk { display: inline-block; width: 8px; height: 8px; border-radius: 50%; background: var(--brand); }

  /* Repair info */
  .repair { position: absolute; left: 0; top: 1020px; width: 1200px; height: 400px; background: var(--white); }
  .repair .section-title { position: absolute; top: 28px; width: 100%; font-size: 24px; }
  .hub { position: absolute; left: 460px; top: 80px; width: 280px; height: 280px; border-radius: 50%; border: 2px solid var(--line); }
  .hub-inner { position: absolute; left: 20px; top: 20px; width: 236px; height: 236px; border-radius: 50%; border: 1px dashed var(--line); text-align: center; padding-top: 66px; }
  .hub-inner h3 { font-family: "Raleway", Arial, sans-serif; font-weight: 400; font-size: 22px; color: var(--brand); margin-bottom: 8px; }
  .hub-inner p { font-size: 10px; color: var(--muted); line-height: 1.5; padding: 0 34px; }
  .service { position: absolute; display: flex; align-items: center; gap: 14px; width: 240px; height: 52px; }
  .service .icon { width: 52px; height: 52px; border-radius: 50%; border: 2px solid var(--line); flex: none; display: flex; align-items: center; justify-content: center; }
  .service h4 { font-family: "Raleway", Arial, sans-serif; font-weight: 400; font-size: 17px; white-space: nowrap; }
  .service p { font-size: 10px; color: var(--muted); white-space: nowrap; }
  .service.is-focus h4 { color: var(--brand); }
  .focus-dot { position: absolute; left: 444px; top: 86px; width: 60px; height: 60px; border-radius: 50%; background: var(--brand); }

  /* About band */
  .about { position: absolute; left: 0; top: 1420px; width: 1200px; height: 392px; background: linear-gradient(180deg, #3db0e0, var(--brand)); color: var(--white); }
  .about-copy { position: absolute; left: 200px; top: 90px; width: 420px; }
  .about-copy h2 { font-family: "Raleway", Arial, sans-serif; font-weight: 400; font-size: 34px; margin-bottom: 8px; }
  .about-copy h3 { font-size: 15px; font-weight: 600; line-height: 1.35; margin-bottom: 10px; }
  .about-copy p { font-size: 11px; line-height: 1.6; opacity: .9; margin-bottom: 16px; }
  .about .btn { background: transparent; border: 1px solid var(--white); }
  .device-photo { position: absolute; left: 630px; top: 90px; width: 360px; height: 200px; border-radius: 20px; background: linear-gradient(150deg, #2a2f35, #5d6670); transform: rotate(-8deg); }

  /* Reviews */
  .reviews { position: absolute; left: 0; top: 1812px; width: 1200px; height: 348px; background: linear-gradient(120deg, var(--review-a), var(--review-b) 60%, #e0cf9a); }
  .reviews .section-title { position: absolute; top: 30px; width: 100%; color: var(--white); }
  .review { position: absolute; top: 100px; width: 216px; height: 216px; border-radius: 50%; background: var(--white); text-align: center; padding: 44px 28px 0; }
  .stars { display: flex; justify-content: center; gap: 3px; margin-bottom: 10px; }
  .review p { font-size: 10px; line-height: 1.5; color: var(--muted); font-style: italic; margin-bottom: 10px; }
  .review cite { font-style: normal; font-size: 11px; font-weight: 700; color: var(--ink); }

  /* Footer */
  .site-footer { position: absolute; left: 0; top: 2160px; width: 1200px; height: 124px; background: var(--white); }
  .footer-links { position: absolute; left: 200px; top: 34px; font-size: 13px; color: var(--ink); }
  .footer-links span { margin: 0 6px; color: var(--muted); }
  .copyright { position: absolute; left: 200px; top: 60px; font-size: 10px; color: var(--muted); }
  .social { position: absolute; left: 612px; top: 32px; display: flex; gap: 6px; }
  .social i { width: 20px; height: 20px; border-radius: 50%; background: var(--brand); display: block; }
  .social i:nth-child(3) { background: #3b5998; }
  .social i:nth-child(4) { background: #d23c3c; }
  .payments { position: absolute; left: 770px; top: 34px; display: flex; gap: 8px; }
  .payments i { width: 36px; height: 22px; border-radius: 3px; background: #e6e8ea; display: block; }
</style>
</head>
<body>

<header class="site-header">
  <div class="brand"><span class="brand-mark"></span><span class="brand-name">Brisk Mend</span></div>
  <div class="call"><small>Call Us Now</small><strong>555.014.2387</strong></div>
</header>

<nav class="main-nav">
  <ul>
    <li class="active">HOME</li><li>REPAIR</li><li>PROTECT</li><li>ABOUT</li><li>CONTACT</li>
  </ul>
</nav>

<section class="hero" role="img" aria-label="Photo of hands holding a smartphone outdoors">
  <svg class="hero-arrow" style="left:90px" width="20" height="36" viewBox="0 0 20 36"><path d="M17 2 3 18l14 16" fill="none" stroke="#fff" stroke-width="3"/></svg>
  <svg class="hero-arrow" style="left:1090px" width="20" height="36" viewBox="0 0 20 36"><path d="M3 2l14 16L3 34" fill="none" stroke="#fff" stroke-width="3"/></svg>
  <div class="hero-copy">
    <h1>Peace of mind</h1>
    <p>Your phone protected against drops, spills and breakdowns, with fast repairs from our local shops.</p>
    <ul>
      <li><span class="tick"></span>Cracked and broken screens covered</li>
      <li><span class="tick"></span>Liquid damage and mechanical faults</li>
      <li><span class="tick"></span>Next day replacement nationwide</li>
    </ul>
  </div>
  <div class="quote-box">
    <div class="label">Price per month</div>
    <div class="price"><small>from</small> $6.99 a month</div>
    <span class="btn">Get a Quote</span>
  </div>
</section>

<section class="pricing">
  <h2 class="section-title">Price Comparison Chart</h2>
  <table class="compare">
    <tr>
      <th class="corner"></th>
      <th><span>PACKAGE NAME</span><b>$7.25</b></th>
      <th><span>PACKAGE NAME</span><b>$6.25</b></th>
      <th class="plan-best"><span>PACKAGE NAME</span><b>$5.99</b></th>
    </tr>
    <tr><td class="row-label">Accidental damage</td><td><i class="chk"></i></td><td><i class="chk"></i></td><td><i class="chk"></i></td></tr>
    <tr><td class="row-label">Mechanical breakdown</td><td><i class="chk"></i></td><td><i class="chk"></i></td><td><i class="chk"></i></td></tr>
    <tr><td class="row-label">Liquid damage</td><td><i class="chk"></i></td><td><i class="chk"></i></td><td><i class="chk"></i></td></tr>
    <tr><td class="row-label">Theft and loss</td><td>Yes</td><td>Yes</td><td>Yes</td></tr>
    <tr><td class="row-label">Deductible</td><td>$99</td><td>$79</td><td>$49</td></tr>
    <tr><td class="row-label">Claims per year</td><td>2 per year</td><td>2 per year</td><td>3 per year</td></tr>
    <tr><td class="row-label">Repair turnaround</td><td>3 days</td><td>2 days</td><td>Next day</td></tr>
    <tr><td class="row-label">Worldwide cover</td><td><i class="chk"></i></td><td><i class="chk"></i></td><td><i class="chk"></i></td></tr>
    <tr><td class="row-label">Cancel anytime</td><td>Yes</td><td>Yes</td><td>Yes</td></tr>
    <tr><td class="row-label">Extras</td><td>Free screen protector</td><td>Free screen protector</td><td>Free screen protector</td></tr>
  </table>
</section>

<section class="repair">
  <h2 class="section-title">Repair Information</h2>
  <svg class="abs" style="left:0;top:0" width="1200" height="400" viewBox="0 0 1200 400">
    <g stroke="#dfe3e6" stroke-width="2" fill="none">
      <path d="M426 220H462"/>
      <path d="M426 332H516"/>
      <path d="M694 116H766"/>
      <path d="M740 220H766"/>
      <path d="M694 324H766"/>
    </g>
  </svg>
  <div class="hub">
    <div class="hub-inner">
      <h3>Firstly Focus</h3>
      <p>Certified technicians, genuine parts and a warranty on every repair.</p>
    </div>
  </div>
  <div class="focus-dot"></div>
  <div class="service is-focus" style="left:200px;top:90px;width:236px"><div><h4>Firstly Focus</h4><p>Same day repair in store</p></div></div>
  <div class="service" style="left:180px;top:194px"><span class="icon"><svg width="22" height="22" viewBox="0 0 22 22"><circle cx="11" cy="11" r="8" fill="none" stroke="#34a6d7" stroke-width="2"/><path d="M11 6v5l3 2" stroke="#34a6d7" stroke-width="2" fill="none"/></svg></span><div><h4>Next Day Claims</h4><p>Replacement delivered fast</p></div></div>
  <div class="service" style="left:180px;top:306px"><span class="icon"><svg width="22" height="22" viewBox="0 0 22 22"><path d="M11 3c4 5 6 8 6 11a6 6 0 0 1-12 0c0-3 2-6 6-11z" fill="none" stroke="#34a6d7" stroke-width="2"/></svg></span><div><h4>Water Damaged</h4><p>Drying and board recovery</p></div></div>
  <div class="service" style="left:770px;top:90px"><span class="icon"><svg width="22" height="22" viewBox="0 0 22 22"><rect x="6" y="2" width="10" height="18" rx="2" fill="none" stroke="#34a6d7" stroke-width="2"/></svg></span><div><h4>Cracked screens</h4><p>Glass and LCD replacement</p></div></div>
  <div class="service" style="left:770px;top:194px"><span class="icon"><svg width="22" height="22" viewBox="0 0 22 22"><circle cx="11" cy="11" r="4" fill="none" stroke="#34a6d7" stroke-width="2"/><path d="M11 2v4M11 16v4M2 11h4M16 11h4" stroke="#34a6d7" stroke-width="2"/></svg></span><div><h4>Technical problem</h4><p>Diagnostics at no charge</p></div></div>
  <div class="service" style="left:770px;top:298px"><span class="icon"><svg width="22" height="22" viewBox="0 0 22 22"><path d="M11 2l7 3v6c0 4-3 7-7 9-4-2-7-5-7-9V5z" fill="none" stroke="#34a6d7" stroke-width="2"/></svg></span><div><h4>Protection</h4><p>Plans for every device</p></div></div>
</section>

<section class="about">
  <div class="about-copy">
    <h2>Brisk Mend</h2>
    <h3>Trusted repair shops across the bay area, now protecting phones and tablets for teams of every size.</h3>
    <p>From a single cracked screen to a fleet of company devices, our technicians keep your people connected with quick turnaround and clear pricing.</p>
    <span class="btn">Read More</span>
  </div>
  <div class="device-photo" role="img" aria-label="Photo of a smartphone with a cracked screen"></div>
</section>

<section class="reviews" role="img" aria-label="Photo of a person using a tablet, behind customer reviews">
  <h2 class="section-title">Our Customer Reviews</h2>
  <div class="review" style="left:160px">
    <div class="stars"><svg width="100" height="16" viewBox="0 0 100 16"><g fill="#f5b800"><path id="s" d="M8 0l2.4 5 5.6.8-4 3.9 1 5.5L8 12.6 3 15.2l1-5.5-4-3.9L5.6 5z"/><use href="#s" x="21"/><use href="#s" x="42"/><use href="#s" x="63"/><use href="#s" x="84"/></g></svg></div>
    <p>"My screen was fixed in under an hour. Friendly staff and fair prices."</p><cite>Dana Whitlow</cite>
  </div>
  <div class="review" style="left:420px">
    <div class="stars"><svg width="100" height="16" viewBox="0 0 100 16"><g fill="#f5b800"><use href="#s"/><use href="#s" x="21"/><use href="#s" x="42"/><use href="#s" x="63"/><use href="#s" x="84"/></g></svg></div>
    <p>"The plan paid off the first week. Claim was simple and quick."</p><cite>Dana Whitlow</cite>
  </div>
  <div class="review" style="left:680px">
    <div class="stars"><svg width="100" height="16" viewBox="0 0 100 16"><g fill="#f5b800"><use href="#s"/><use href="#s" x="21"/><use href="#s" x="42"/><use href="#s" x="63"/><use href="#s" x="84"/></g></svg></div>
    <p>"They saved my phone after a pool accident. Highly recommended."</p><cite>Dana Whitlow</cite>
  </div>
  <div class="review" style="left:940px">
    <div class="stars"><svg width="100" height="16" viewBox="0 0 100 16"><g fill="#f5b800"><use href="#s"/><use href="#s" x="21"/><use href="#s" x="42"/><use href="#s" x="63"/><use href="#s" x="84"/></g></svg></div>
    <p>"Our whole office is covered now. Great service every time."</p><cite>Dana Whitlow</cite>
  </div>
</section>

<footer class="site-footer">
  <div class="footer-links">Home<span>|</span>Repair<span>|</span>Protect<span>|</span>About<span>|</span>Contact</div>
  <div class="copyright">© 2015 Brisk Mend. All rights reserved.</div>
  <div class="social"><i></i><i></i><i></i><i></i></div>
  <div class="payments"><i></i><i></i><i></i><i></i><i></i></div>
</footer>

</body>
</html>
```